Marlow Hire Business Card for recruitment company

We are looking for a Business Card Design that incorporates our personal details and our busines name and logo. We are a specialized search consultancy that recruit Property and Construction professionals.
We would like a business card that stands out and is appealing to the Construction and Property industry as well.

Target Market(s)

people in the construction and property industry

Contact Information for Business Card

Business Name and logo

Font styles to use
Serif

Colors
0094D4
00A9DD
6FCCEA
C7EBF8
E9F6FB

Requirements
Must have
• Business name and logo as well as contact details
Should not have
• No photos of us please

```html
<!DOCTYPE html>
<html lang="en">
<head>
<meta charset="utf-8">
<title>Marlow Hire – Business Card</title>
<link rel="stylesheet" href="https://fonts.googleapis.com/css2?family=Arimo:wght@400;700&family=Josefin+Sans:wght@300&display=swap">
<style>
  :root {
    --backdrop: #e6e6e4;
    --card-navy: #033f56;
    --mark-tone: #1c5569;
    --mark-bright: #2b87a5;
    --ink-light: #ffffff;
    --ink-soft: #d9e6ec;
  }
  * { margin: 0; padding: 0; box-sizing: border-box; }
  html, body { width: 1200px; height: 801px; overflow: hidden; }
  body {
    background: var(--backdrop);
    font-family: "Arimo", Arial, sans-serif;
    position: relative;
  }
  .card {
    position: absolute;
    top: 232px;
    width: 540px;
    height: 320px;
    background: var(--card-navy);
    color: var(--ink-light);
    overflow: hidden;
    box-shadow: 0 6px 18px rgba(0,0,0,0.18);
  }
  .card--front { left: 40px; }
  .card--back { left: 620px; }

  .brand-name {
    font-family: "Josefin Sans", Arial, sans-serif;
    font-weight: 300;
    letter-spacing: 0.06em;
    text-transform: uppercase;
    color: var(--ink-light);
    white-space: nowrap;
  }

  .decor-area {
    position: absolute;
    top: 0;
    height: 320px;
  }
  .card--front .decor-area {
    right: 0; width: 260px;
    background: linear-gradient(90deg, rgba(28,85,105,0) 0%, rgba(28,85,105,0.55) 100%);
  }
  .card--back .decor-area {
    left: 0; width: 300px;
    background: linear-gradient(90deg, rgba(43,135,165,0.45) 0%, rgba(43,135,165,0) 100%);
  }

  .card--front .brand-name {
    position: absolute; left: 38px; top: 42px; font-size: 40px;
  }
  .person { position: absolute; left: 40px; top: 150px; }
  .person__name { font-weight: 700; font-size: 19px; letter-spacing: 0.02em; text-transform: uppercase; }
  .person__role { font-size: 14px; margin-top: 2px; }

  .contact-list { position: absolute; left: 40px; top: 208px; list-style: none; }
  .contact-list li {
    display: flex; align-items: center; gap: 10px;
    font-size: 15px; line-height: 24px;
  }
  .contact-list svg { width: 14px; height: 14px; flex: none; }

  .address {
    position: absolute; right: 34px; top: 120px;
    font-size: 13px; line-height: 18px; text-align: right; color: var(--ink-soft);
  }

  .card--back .brand-name {
    position: absolute; right: 32px; bottom: 52px; font-size: 42px;
  }
</style>
</head>
<body>

  <section class="card card--front" aria-label="Business card front">
    <div class="decor-area" role="img" aria-label="Area for a faint brand decoration"></div>
    <div class="brand-name">Marlow Hire</div>

    <div class="person">
      <div class="person__name">Elias Granger</div>
      <div class="person__role">Manager</div>
    </div>

    <ul class="contact-list">
      <li>
        <svg viewBox="0 0 16 16" aria-hidden="true"><path fill="#fff" d="M4 1l3 3-1.6 1.8c.8 1.9 2.6 3.7 4.6 4.6L11.8 9 15 12l-2 3C7 15 1 9 1 3z"/></svg>
        555-014-2100
      </li>
      <li>
        <svg viewBox="0 0 16 16" aria-hidden="true"><rect x="1.5" y="3.5" width="13" height="9" fill="none" stroke="#fff" stroke-width="1.4"/><path d="M1.5 3.5L8 9l6.5-5.5" fill="none" stroke="#fff" stroke-width="1.4"/></svg>
        elias@marlowhire.co
      </li>
      <li>
        <svg viewBox="0 0 16 16" aria-hidden="true"><circle cx="8" cy="8" r="6.5" fill="none" stroke="#fff" stroke-width="1.4"/><ellipse cx="8" cy="8" rx="2.8" ry="6.5" fill="none" stroke="#fff" stroke-width="1.2"/><path d="M1.5 8h13M2.5 5h11M2.5 11h11" stroke="#fff" stroke-width="1.1"/></svg>
        www.marlowhire.co
      </li>
    </ul>

    <p class="address">Your address, city<br>state, ZIP 0000</p>
  </section>

  <section class="card card--back" aria-label="Business card back">
    <div class="decor-area" role="img" aria-label="Area for a large brand decoration in bright blue"></div>
    <div class="brand-name">Marlow Hire</div>
  </section>

</body>
</html>
```